Business card for marketing analytics company

Need a business card for new company. I have a logo already that I want to be built into the card and should use those colours

Company is called steered by tallies
Design must bring steered by tallies to life not be a card that could be for anyone with a logo put on it.

Like the front to be fairly clean and uncluttered bringing the logo out with a suitable design on the back of the card.

The logo represents a compass and business growth so those themes along with numbers, analytics , data are appropriate.
I'm often working with creative industries so also needs to reflect the creative side of analytics rather than be very corporate looking.

Target Market(s)

Ad agency, media agency, consumer goods clients

Industry/Entity Type

Market Research

Contact Information for Business Card

Needs to include name, title, email and phone number

Colors
f78f20
f68d4d
ec1f27

Requirements
Must have
• Must bring steered by tallies to life not be a card that could be for anyone with a logo put on it.
• Logo, Correct colours
• Like a design on the back that relates to company name
• Designs for both sides
Should not have
• Please do not just submit logo and a coloured card.
• It needs to have a design element to it
• No black background
• No clear cards - needs front & back

```html
<!DOCTYPE html>
<html lang="en">
<head>
<meta charset="utf-8">
<title>Steered by Tallies – Business Card</title>
<link href="https://fonts.googleapis.com/css2?family=Montserrat:wght@600&family=Roboto:wght@400;500;700&display=swap" rel="stylesheet">
<style>
  :root {
    --backdrop: #4a4a4a;
    --brand-orange: #f37324;
    --brand-red: #c4222a;
    --ink-slate: #4b5560;
    --card-white: #ffffff;
    --faint-ring-light: rgba(255,255,255,0.12);
    --faint-ring-grey: #f1f0f0;
  }
  * { box-sizing: border-box; margin: 0; padding: 0; }
  html, body { width: 900px; height: 1200px; overflow: hidden; }
  body { background: var(--backdrop); position: relative; font-family: "Roboto", Arial, sans-serif; }

  .card {
    position: absolute; left: 117px; width: 672px; height: 394px;
    border-radius: 18px; overflow: hidden;
  }
  .card--front { top: 176px; background: var(--brand-orange); }
  .card--back  { top: 631px; background: var(--card-white); }

  .card__deco { position: absolute; }
  .card--front .card__deco { left: 368px; top: 20px; }
  .card--back .card__deco { left: -40px; top: 10px; }

  .front-mark {
    position: absolute; left: 50px; top: 244px;
    display: flex; align-items: center; gap: 22px;
  }
  .front-mark__dot {
    width: 90px; height: 90px; border-radius: 50%;
    border: 4px solid var(--card-white);
  }
  .front-mark__name {
    font-family: "Montserrat", Arial, sans-serif; font-weight: 600;
    font-size: 27px; line-height: 30px; color: var(--card-white);
  }

  .back-name {
    position: absolute; left: 48px; top: 54px;
    font-family: "Montserrat", Arial, sans-serif; font-weight: 600;
    font-size: 45px; line-height: 50px; color: var(--ink-slate);
  }
  .back-name__line2 { display: block; padding-left: 72px; }

  .person { position: absolute; left: 97px; top: 172px; }
  .person__name { font-size: 24px; font-weight: 700; color: var(--ink-slate); line-height: 28px; }
  .person__title { font-size: 18px; font-weight: 500; color: var(--brand-orange); line-height: 22px; }

  .address {
    position: absolute; left: 131px; top: 238px;
    font-size: 16px; line-height: 22px; color: var(--ink-slate); font-style: normal; font-weight: 500;
  }
  .contact { position: absolute; left: 173px; top: 295px; list-style: none; }
  .contact__item {
    display: flex; align-items: center; gap: 7px;
    font-size: 16px; line-height: 22px; color: var(--ink-slate); font-weight: 500;
  }
  .contact__icon { width: 15px; height: 15px; fill: var(--brand-orange); }

  .back-ring {
    position: absolute; left: 410px; top: 96px;
    width: 200px; height: 200px; border-radius: 50%;
    border: 6px solid var(--brand-red);
  }
</style>
</head>
<body>

<section class="card card--front" aria-label="Card front">
  <svg class="card__deco" width="420" height="420" aria-hidden="true">
    <circle cx="210" cy="200" r="180" fill="none" stroke="var(--faint-ring-light)" stroke-width="14"/>
  </svg>
  <div class="front-mark">
    <span class="front-mark__dot"></span>
    <span class="front-mark__name">Steered by<br>Tallies</span>
  </div>
</section>

<section class="card card--back" aria-label="Card back">
  <svg class="card__deco" width="420" height="420" aria-hidden="true">
    <circle cx="190" cy="200" r="175" fill="none" stroke="var(--faint-ring-grey)" stroke-width="14"/>
  </svg>

  <h1 class="back-name">Steered by<span class="back-name__line2">Tallies</span></h1>

  <div class="person">
    <p class="person__name">Martin Keller</p>
    <p class="person__title">General Manager</p>
  </div>

  <address class="address">2210 Harbor Lane Suite 300<br>Elm Ridge, IL 60190</address>

  <ul class="contact">
    <li class="contact__item">
      <svg class="contact__icon" viewBox="0 0 24 24" aria-hidden="true"><path d="M6.6 10.8a15.1 15.1 0 0 0 6.6 6.6l2.2-2.2a1 1 0 0 1 1-.25 11.4 11.4 0 0 0 3.6.57 1 1 0 0 1 1 1V20a1 1 0 0 1-1 1A17 17 0 0 1 3 4a1 1 0 0 1 1-1h3.5a1 1 0 0 1 1 1c0 1.25.2 2.45.57 3.57a1 1 0 0 1-.25 1z"/></svg>
      0744-615-292
    </li>
    <li class="contact__item">
      <svg class="contact__icon" viewBox="0 0 24 24" aria-hidden="true"><path d="M2 5h20v14H2z M3.5 6.5 12 13l8.5-6.5" stroke="#fff" stroke-width="1.5"/></svg>
      mkeller@tallyco.com
    </li>
  </ul>

  <span class="back-ring" aria-hidden="true"></span>
</section>

</body>
</html>
```